The Pixel Tap Business card.

A Simple card with our Logo and contact information. To give to investors and other professionals.

We are a nerd themed bar.
our target market is young professionals age 21+ but the real purpose of this business card is to present to potential investors and other professionals with our contact information. as we are still looking for funding before we start up.

I am partial to green and my partner likes red we are open to iteration.

Target Market(s)

Investors

Industry/Entity Type

Business

Contact Information for Business Card

Martin Hale (225) 730-6192 kent.h4711@mailnest.test Glen Porter (225) 968-5037 glenp318@mailnest.test

Font styles to use
Serif

Requirements
Nice to have
• Keep it simple but not boring.
• Use the Logos but feel free to edit them to match theme/colors.
• Keep the back clean and use one of the Logos.

```html
<!DOCTYPE html>
<html lang="en">
<head>
<meta charset="utf-8">
<title>The Pixel Tap – Business Card</title>
<link rel="stylesheet" href="https://fonts.googleapis.com/css2?family=Marcellus&display=swap">
<style>
  :root {
    --ink: #0b0b0b;
    --paper: #f4f4f4;
    --stage: #d9d6d1;
    --red-deep: #d8463c;
    --red-mid: #e7837c;
    --red-soft: #f2c1bd;
    --white: #ffffff;
    --serif: "Marcellus", "Times New Roman", serif;
  }
  * { box-sizing: border-box; margin: 0; padding: 0; }
  html, body {
    width: 1200px; height: 780px; overflow: hidden;
    background: var(--stage);
  }
  .stage {
    position: relative; width: 1200px; height: 780px;
    display: flex; align-items: center; justify-content: center; gap: 28px;
  }
  .card {
    position: relative; width: 560px; height: 320px; overflow: hidden;
    box-shadow: 0 6px 18px rgba(0,0,0,.22);
  }
  .card-front { background: var(--ink); }
  .card-back { background: var(--paper); }
  .card-art { position: absolute; inset: 0; width: 100%; height: 100%; }

  .brand {
    position: absolute; display: flex; align-items: center; gap: 12px;
    font-family: var(--serif); letter-spacing: .08em; text-transform: uppercase;
    white-space: nowrap;
  }
  .brand-dot { width: 20px; height: 20px; border-radius: 50%; background: var(--red-deep); flex: none; }
  .brand-name { line-height: 1; }
  .card-front .brand { right: 84px; top: 66px; color: var(--white); font-size: 30px; }
  .card-back .brand { left: 0; right: 0; top: 138px; justify-content: center; color: var(--ink); font-size: 40px; }

  .contacts {
    position: absolute; left: 40px; top: 122px; color: var(--white);
    font-family: var(--serif);
  }
  .contact + .contact { margin-top: 12px; }
  .contact-name { display: flex; align-items: center; gap: 8px; font-size: 19px; line-height: 1.15; white-space: nowrap; }
  .contact-line { font-size: 13px; line-height: 1.35; letter-spacing: .02em; white-space: nowrap; }
  .icon-box {
    width: 16px; height: 16px; background: var(--white);
    display: inline-flex; align-items: center; justify-content: center;
  }
  .icon-box svg { width: 12px; height: 12px; }
</style>
</head>
<body>
<main class="stage">

  <section class="card card-front" aria-label="Business card front">
    <svg class="card-art" viewBox="0 0 560 320" aria-hidden="true">
      <defs>
        <linearGradient id="redBandFront" x1="0" y1="0" x2="0" y2="1">
          <stop offset="0" stop-color="var(--red-soft)"/>
          <stop offset="1" stop-color="var(--red-deep)"/>
        </linearGradient>
        <linearGradient id="redBandTop" x1="0" y1="1" x2="0" y2="0">
          <stop offset="0" stop-color="var(--red-soft)"/>
          <stop offset="1" stop-color="var(--red-deep)"/>
        </linearGradient>
      </defs>
      <polygon points="0,0 300,0 262,38 0,38" fill="url(#redBandTop)"/>
      <polygon points="0,38 262,38 300,0 314,0 268,46 0,46" fill="var(--white)"/>
      <polygon points="0,262 404,262 468,198 560,198 560,320 0,320" fill="var(--white)"/>
      <polygon points="0,270 408,270 472,206 560,206 560,320 0,320" fill="url(#redBandFront)"/>
      <g fill="var(--white)">
        <polygon points="340,0 364,0 330,34 306,34"/>
        <polygon points="384,0 408,0 374,34 350,34"/>
        <polygon points="428,0 452,0 418,34 394,34"/>
        <polygon points="472,0 496,0 462,34 438,34"/>
        <polygon points="560,92 560,116 520,156 496,156"/>
        <polygon points="560,132 560,156 538,178 514,178"/>
        <polygon points="560,52 560,76 540,96 516,96"/>
      </g>
    </svg>

    <div class="brand"><span class="brand-dot"></span><span class="brand-name">The Pixel Tap</span></div>

    <div class="contacts">
      <div class="contact">
        <p class="contact-name">Glen Porter
          <span class="icon-box"><svg viewBox="0 0 16 16"><path d="M4 1.5l2.4 3-1.5 1.6a9 9 0 0 0 5 5l1.6-1.5 3 2.4-1.6 2.5C7.5 14.3 1.7 8.5 1.5 3.1z" fill="var(--ink)"/></svg></span>
          <span class="icon-box"><svg viewBox="0 0 16 16"><rect x="1.5" y="3.5" width="13" height="9" fill="none" stroke="var(--ink)" stroke-width="1.6"/><path d="M1.5 3.5L8 9l6.5-5.5" fill="none" stroke="var(--ink)" stroke-width="1.6"/></svg></span>
        </p>
        <p class="contact-line">(225) 968-5037</p>
        <p class="contact-line">glenp318@mailnest.test</p>
      </div>
      <div class="contact">
        <p class="contact-name">Martin Hale
          <span class="icon-box"><svg viewBox="0 0 16 16"><path d="M4 1.5l2.4 3-1.5 1.6a9 9 0 0 0 5 5l1.6-1.5 3 2.4-1.6 2.5C7.5 14.3 1.7 8.5 1.5 3.1z" fill="var(--ink)"/></svg></span>
          <span class="icon-box"><svg viewBox="0 0 16 16"><rect x="1.5" y="3.5" width="13" height="9" fill="none" stroke="var(--ink)" stroke-width="1.6"/><path d="M1.5 3.5L8 9l6.5-5.5" fill="none" stroke="var(--ink)" stroke-width="1.6"/></svg></span>
        </p>
        <p class="contact-line">(225) 730-6192</p>
        <p class="contact-line">kent.h4711@mailnest.test</p>
      </div>
    </div>
  </section>

  <section class="card card-back" aria-label="Business card back">
    <svg class="card-art" viewBox="0 0 560 320" aria-hidden="true">
      <defs>
        <linearGradient id="redBandBack" x1="0" y1="0" x2="0" y2="1">
          <stop offset="0" stop-color="var(--red-deep)"/>
          <stop offset="1" stop-color="var(--red-soft)"/>
        </linearGradient>
        <linearGradient id="redBandSide" x1="0" y1="0" x2="1" y2="0">
          <stop offset="0" stop-color="var(--red-deep)"/>
          <stop offset="1" stop-color="var(--red-soft)"/>
        </linearGradient>
      </defs>
      <polygon points="0,0 560,0 560,52 126,52 76,102 0,102" fill="url(#redBandBack)"/>
      <polyline points="560,58 128,58 78,108 0,108" fill="none" stroke="var(--ink)" stroke-width="8"/>
      <polygon points="0,108 28,108 28,320 0,320" fill="url(#redBandSide)"/>
      <g fill="var(--ink)">
        <polygon points="150,320 176,320 212,284 186,284"/>
        <polygon points="196,320 222,320 258,284 232,284"/>
        <polygon points="242,320 268,320 304,284 278,284"/>
        <polygon points="560,220 560,246 486,320 460,320"/>
        <polygon points="560,264 560,290 530,320 504,320"/>
      </g>
    </svg>

    <div class="brand"><span class="brand-dot"></span><span class="brand-name">The Pixel Tap</span></div>
  </section>

</main>
</body>
</html>
```